現在ホームページリニューアルを検討しております。
社内でのデザインだとどうしても前情報がある分、発想の限界、偏りがどうしてもあります。

今回はなるべくフラットな状態でデザインを検討したいと考えておりますので、こちらで公募をさせていただくことにしました。

既存の歯科医院のデザインやイメージに縛られることなく、自由な発想でご提案頂きたいと思っております。

■依頼内容

PC・スマートフォン用 それぞれ1枚 合計2枚
(実装する際にはレスポンシブの予定です。)

診療科目は
小児
一般
矯正(大学から月に数回先生にお越し頂いています)

医院の特徴
ショッピングモール内にあります
駐車場あり
バリアフリー
お子さんの遊びスペースあり
デザイナー物件

ページ数
2ページ
希望イメージ
シンプル 複雑
単色 カラフル
暗い 明るい
日常 高級
遊び心 厳粛
未来的 伝統的
女性的 男性的
納品ファイル
• 高解像度JPG (.jpg)
• フォトショップ形式 (.psd)
• PNG形式 (.png)
▼弊社が用意するもの
・ページ構成
・テキスト
・ワイヤーフレーム
・ロゴ
・写真
※受注者様のご意向があれば、ビデオ通話などで対応することも可能です。
※ページ構成や画像などは、個別に送らせていただきたいので、まずはご提案またはメッセージにてご連絡ください。

▼依頼の流れ
1.ご提案
ご提案をいただき次第、弊社よりTOPページの構成をお送りします。
3.デザイン作成
デザインを作成しましたら、提案の【追記する】からデザインファイルの追加をしてください。
5.修正依頼
修正していただきたい箇所がある場合は、修正依頼をいたしますので、修正案を再提案してください。
6.納品
フォトショップ(psd)またはイラストレーター(ai)形式で納品をしていただきます。納品が完了次第、当選を行います。

弊社では、複数のWEBサイトを運用しております。
今回はTOPページのみの依頼となっておりますが、継続的に依頼をさせていただくことも考えております。
ご提案をお待ちしております。
ワイヤーフレームと写真素材を添付します。
依頼金額を45000円に変更して、延長しました。
たくさんのご応募ありがとうございます。
現在、選考中です。3~7日程度で当選デザインを決定できるかと思いますので、今しばらくお待ちください。

歯科医院スタッフの投票にて決定いたしました。

たくさんのご提案ありがとうございます。また機会があれば、是非よろしくお願いいたします。

```html
<!DOCTYPE html>
<html lang="ja">
<head>
<meta charset="utf-8">
<title>はるの歯科</title>
<link rel="stylesheet" href="https://fonts.googleapis.com/css2?family=Noto+Sans+JP:wght@300;400;500&family=Quicksand:wght@500;700&display=swap">
<style>
:root{
  --teal:#5fcfb3;
  --teal-dark:#3fb89c;
  --mint:#d6f6ee;
  --sky:#d3eefa;
  --text:#3d3d3d;
  --sub:#6b6b6b;
  --line:#e2e2e2;
  --date:#8fd3c2;
  --photo-a:#dfe6ea;
  --photo-b:#c9d7df;
}
*{margin:0;padding:0;box-sizing:border-box}
html,body{width:1200px;height:5382px;overflow:hidden;background:#fff}
body{position:relative;font-family:"Noto Sans JP",sans-serif;color:var(--text)}
.abs{position:absolute}
.en{font-family:"Quicksand",sans-serif}
.grad{background:linear-gradient(90deg,var(--mint),var(--sky))}
.photo{position:absolute;background:linear-gradient(135deg,var(--photo-a),var(--photo-b))}
.btn{position:absolute;display:flex;align-items:center;justify-content:center;gap:12px;border-radius:40px;font-size:20px;color:#fff;background:linear-gradient(90deg,#7fe0c6,#9fe3ef)}
.btn .dot{width:24px;height:24px;border-radius:50%;background:#fff;display:flex;align-items:center;justify-content:center}
.outline-btn{position:absolute;display:flex;align-items:center;justify-content:center;gap:10px;border:2px solid var(--teal);border-radius:40px;color:var(--teal-dark);background:#fff;font-family:"Quicksand",sans-serif;font-weight:700;letter-spacing:.08em}
.arrow-c{width:20px;height:20px;border-radius:50%;border:1.5px solid var(--teal);display:inline-flex;align-items:center;justify-content:center}
.sec-head{position:absolute;display:flex;align-items:flex-start;gap:14px}
.sec-head .mark{width:44px;height:44px;border:2px solid var(--teal);border-radius:50%;margin-top:6px}
.sec-head small{display:block;font-family:"Quicksand",sans-serif;color:var(--teal-dark);font-size:14px}
.sec-head h2{font-weight:400;font-size:29px;line-height:1.3}
.card{position:absolute;background:#fff;box-shadow:0 6px 24px rgba(0,0,0,.06);padding:42px 40px}
.card .kicker{font-size:17px}
.card .kicker span{font-size:13px;color:var(--sub)}
.card h3{font-weight:400;font-size:27px;line-height:1.6;margin-top:18px;display:flex;gap:14px}
.card h3 i{font-style:normal;font-family:"Quicksand",sans-serif;color:var(--teal);font-size:20px;padding-top:6px}
.card p{font-size:15px;line-height:1.7;color:var(--sub);margin-top:18px}
.treat .img{position:absolute;width:217px;height:220px}
.treat .name{position:absolute;font-size:15px;color:var(--teal-dark);display:flex;gap:6px;align-items:center}
.treat .desc{position:absolute;font-size:15px}
.news li{list-style:none;display:flex;gap:28px;font-size:15px;height:51px;align-items:center}
.news time{color:var(--date);font-family:"Quicksand",sans-serif}
.hours{border-collapse:collapse;font-size:15px}
.hours td,.hours th{width:46px;height:46px;text-align:center;font-weight:400;border-bottom:1px solid var(--line)}
.hours th{border-left:1px solid var(--line)}
.hours td:first-child{width:120px;border-left:none}
.fnav h4{font-weight:400;font-size:17px;margin-bottom:22px}
.fnav li{list-style:none;font-size:16px;margin-bottom:18px;display:flex;gap:8px;align-items:center}
</style>
</head>
<body>

<!-- header -->
<div class="abs" style="left:0;top:0;width:260px;height:260px;background:#fff;z-index:3;display:flex;flex-direction:column;align-items:center;justify-content:center;gap:18px">
  <div style="width:78px;height:78px;border-radius:50%;background:var(--teal)"></div>
  <div style="font-size:24px;font-weight:500;text-align:center;line-height:1.3">HARUNO<br>DENTAL CLINIC</div>
</div>
<div class="abs" style="left:286px;top:52px;display:flex;gap:14px;align-items:center">
  <svg width="26" height="26" viewBox="0 0 24 24"><path d="M6.6 10.8a15 15 0 0 0 6.6 6.6l2.2-2.2c.3-.3.7-.4 1-.2 1.1.4 2.3.6 3.6.6.6 0 1 .4 1 1V20c0 .6-.4 1-1 1A17 17 0 0 1 3 4c0-.6.4-1 1-1h3.5c.6 0 1 .4 1 1 0 1.3.2 2.5.6 3.6.1.3 0 .7-.2 1z" fill="var(--teal)"/></svg>
  <span style="font-size:33px;font-weight:300">000-555-0123</span>
</div>
<div class="abs" style="left:566px;top:54px;font-size:15px;line-height:1.5">9:00-13:00 / 14:30-18:30<br>休診日：日・祝および水・土</div>
<div class="btn" style="left:872px;top:42px;width:272px;height:66px">WEB予約はこちら<span class="dot"><svg width="10" height="10"><path d="M3 1l4 4-4 4" stroke="var(--teal)" stroke-width="1.8" fill="none"/></svg></span></div>

<!-- hero -->
<div class="abs grad" style="left:0;top:605px;width:1200px;height:230px"></div>
<div class="photo" role="img" aria-label="明るい診療室と歯科チェアの写真" style="left:77px;top:150px;width:1067px;height:591px;background:linear-gradient(120deg,#e9ecde,#d8e2e6 50%,#eef1f1)"></div>
<div class="photo" role="img" aria-label="院内の小さな写真1" style="left:77px;top:700px;width:177px;height:93px;background:#b9c7b8"></div>
<div class="photo" role="img" aria-label="院内の小さな写真2" style="left:277px;top:700px;width:177px;height:93px;background:#c4cbd0"></div>
<div class="abs" style="left:720px;top:313px;width:424px;height:522px;background:rgba(255,255,255,.72);border-radius:200px 200px 0 0"></div>
<div class="abs" style="left:720px;top:425px;width:420px;text-align:center;font-size:42px;font-weight:300;line-height:1.5;letter-spacing:.05em">痛くない<br>歯科治療</div>
<div class="outline-btn" style="left:772px;top:586px;width:288px;height:59px;font-family:'Noto Sans JP',sans-serif;font-weight:400;font-size:18px;letter-spacing:.04em">治療シュミレーション<span class="arrow-c"><svg width="8" height="8"><path d="M2 1l3 3-3 3" stroke="var(--teal)" stroke-width="1.5" fill="none"/></svg></span></div>

<!-- treatment -->
<div class="sec-head" style="left:52px;top:910px"><div class="mark"></div><div><small>Treatment</small><h2>治療について</h2></div></div>
<div class="abs" style="left:125px;top:1000px;height:280px;writing-mode:vertical-rl;font-size:15px;line-height:1.75;letter-spacing:.06em">コンセプトメッセージが入ります。コンセプトメッセージが入ります。コンセプトメッセージが入ります。コンセプトメッセージが入ります。</div>
<div class="abs" style="left:1144px;top:918px;width:56px;height:240px;background:linear-gradient(180deg,#8fe2cc,#a7e2f1);border-radius:10px 0 0 10px;color:#fff;writing-mode:vertical-rl;font-size:15px;display:flex;align-items:center;justify-content:center;letter-spacing:.15em">WEB予約はこちら</div>
<div class="treat">
  <div class="photo img" role="img" aria-label="子どもの歯磨き指導の写真" style="left:403px;top:918px;background:#f2dcc8"></div>
  <div class="photo img" role="img" aria-label="医師が子どもを診察する写真" style="left:643px;top:918px;background:#c8d0dc"></div>
  <div class="photo img" role="img" aria-label="笑顔の女性患者の写真" style="left:883px;top:918px;background:#e6e3e6"></div>
  <div class="photo img" role="img" aria-label="歯を気にする女性の写真" style="left:403px;top:1229px;background:#eadfd7"></div>
  <div class="photo img" role="img" aria-label="入れ歯の写真" style="left:643px;top:1229px;background:#f0dcdc"></div>
  <div class="photo img" role="img" aria-label="歯科治療器具の写真" style="left:883px;top:1229px;background:#dfe5ea"></div>
  <div class="name" style="left:403px;top:1150px">治療名01<span class="arrow-c"><svg width="8" height="8"><path d="M2 1l3 3-3 3" stroke="var(--teal)" stroke-width="1.5" fill="none"/></svg></span></div>
  <div class="name" style="left:643px;top:1150px">治療名02<span class="arrow-c"><svg width="8" height="8"><path d="M2 1l3 3-3 3" stroke="var(--teal)" stroke-width="1.5" fill="none"/></svg></span></div>
  <div class="name" style="left:883px;top:1150px">治療名03<span class="arrow-c"><svg width="8" height="8"><path d="M2 1l3 3-3 3" stroke="var(--teal)" stroke-width="1.5" fill="none"/></svg></span></div>
  <div class="name" style="left:403px;top:1461px">治療名04<span class="arrow-c"><svg width="8" height="8"><path d="M2 1l3 3-3 3" stroke="var(--teal)" stroke-width="1.5" fill="none"/></svg></span></div>
  <div class="name" style="left:643px;top:1461px">治療名05<span class="arrow-c"><svg width="8" height="8"><path d="M2 1l3 3-3 3" stroke="var(--teal)" stroke-width="1.5" fill="none"/></svg></span></div>
  <div class="name" style="left:883px;top:1461px">治療名06<span class="arrow-c"><svg width="8" height="8"><path d="M2 1l3 3-3 3" stroke="var(--teal)" stroke-width="1.5" fill="none"/></svg></span></div>
  <div class="desc" style="left:403px;top:1178px">テキストが入ります。</div>
  <div class="desc" style="left:643px;top:1178px">テキストが入ります。</div>
  <div class="desc" style="left:883px;top:1178px">テキストが入ります。</div>
  <div class="desc" style="left:403px;top:1489px">テキストが入ります。</div>
  <div class="desc" style="left:643px;top:1489px">テキストが入ります。</div>
  <div class="desc" style="left:883px;top:1489px">テキストが入ります。</div>
</div>

<!-- concept -->
<div class="sec-head" style="left:52px;top:1626px"><div class="mark"></div><div><small>Concept</small><h2>コンセプト</h2></div></div>

<div class="abs grad" style="left:359px;top:1690px;width:841px;height:522px"></div>
<div class="photo" role="img" aria-label="女の子を治療する歯科衛生士の写真" style="left:52px;top:1747px;width:628px;height:419px;background:linear-gradient(135deg,#eee9ee,#d9cfe3)"></div>
<div class="card" style="left:618px;top:1789px;width:467px;height:313px">
  <div class="kicker en">Dental Treatment <span>/ 治療</span></div>
  <h3><i>01</i>痛くない歯科治療</h3>
  <p>テキストが入ります。テキストが入ります。<br>テキストが入ります。テキストが入ります。</p>
  <div class="outline-btn" style="position:relative;margin-top:22px;width:158px;height:40px;font-size:15px">VIEW MORE<span class="arrow-c"><svg width="8" height="8"><path d="M2 1l3 3-3 3" stroke="var(--teal)" stroke-width="1.5" fill="none"/></svg></span></div>
</div>

<div class="abs grad" style="left:0;top:2248px;width:939px;height:444px"></div>
<div class="photo" role="img" aria-label="託児スペースのベビーサークルとおもちゃの写真" style="left:515px;top:2304px;width:629px;height:420px;background:linear-gradient(135deg,#e8d7bd,#efe6b8 60%,#c9e3e8)"></div>
<div class="card" style="left:108px;top:2340px;width:468px;height:350px">
  <div class="kicker en">Service <span>/ サービス</span></div>
  <h3><i>02</i>お子様連れでも安心の<br>託児サービス</h3>
  <p>テキストが入ります。テキストが入ります。<br>テキストが入ります。テキストが入ります。</p>
  <div class="outline-btn" style="position:relative;margin-top:22px;width:158px;height:40px;font-size:15px">VIEW MORE<span class="arrow-c"><svg width="8" height="8"><path d="M2 1l3 3-3 3" stroke="var(--teal)" stroke-width="1.5" fill="none"/></svg></span></div>
</div>

<div class="abs grad" style="left:369px;top:2805px;width:831px;height:472px"></div>
<div class="photo" role="img" aria-label="医師と患者の治療風景の写真" style="left:52px;top:2861px;width:628px;height:420px;background:linear-gradient(135deg,#d9dde4,#eef0f2)"></div>
<div class="card" style="left:618px;top:2899px;width:467px;height:348px">
  <div class="kicker en">Policy <span>/ クリニックの方針</span></div>
  <h3><i>03</i>何度も通院しない<br>歯医者さん</h3>
  <p>テキストが入ります。テキストが入ります。<br>テキストが入ります。テキストが入ります。</p>
  <div class="outline-btn" style="position:relative;margin-top:22px;width:158px;height:40px;font-size:15px">VIEW MORE<span class="arrow-c"><svg width="8" height="8"><path d="M2 1l3 3-3 3" stroke="var(--teal)" stroke-width="1.5" fill="none"/></svg></span></div>
</div>

<!-- topics -->
<div class="sec-head" style="left:52px;top:3394px"><div class="mark"></div><div><small>Topics</small><h2>お知らせ</h2></div></div>
<div class="abs" style="left:94px;top:3500px;width:636px;height:305px;background:#fff;box-shadow:0 4px 20px rgba(0,0,0,.07);padding:22px 46px">
  <ul class="news">
    <li><time>2019.00.00</time>ホームページをリニューアルしました。</li>
    <li><time>2019.00.00</time>ホームページをリニューアルしました。</li>
    <li><time>2019.00.00</time>ホームページをリニューアルしました。</li>
    <li><time>2019.00.00</time>ホームページをリニューアルしました。</li>
    <li><time>2019.00.00</time>ホームページをリニューアルしました。</li>
  </ul>
  <div class="abs" style="left:606px;top:40px;width:8px;height:220px;background:#f1f1f1;border-radius:4px"><div style="height:60px;background:#cfcfcf;border-radius:4px"></div></div>
</div>
<div class="photo" role="img" aria-label="白い相談室の写真" style="left:762px;top:3500px;width:158px;height:236px;background:#e9e6df"></div>
<div class="photo" role="img" aria-label="院内廊下の写真" style="left:945px;top:3546px;width:159px;height:238px;background:#e6e3e0"></div>

<!-- message -->
<div class="abs grad" style="left:0;top:4122px;width:835px;height:407px"></div>
<div class="photo" role="img" aria-label="デザイン性の高い診療室の写真" style="left:90px;top:3924px;width:355px;height:532px;background:linear-gradient(160deg,#f3f1ee,#d4d2cf)"></div>
<div class="abs en" style="left:490px;top:3924px;font-size:13px;color:var(--teal-dark)">Message</div>
<div class="abs" style="left:490px;top:3958px;font-size:26px;line-height:1.6">本文から抜粋したタイトルが入ります。<br>本文から抜粋したタイトルが入ります。</div>
<div class="abs" style="left:490px;top:4062px;width:585px;font-size:15px;line-height:2.27;color:#555">ダミーテキストが入ります。ごあいさつのメッセージが入ります。ダミーテキストが入ります。ごあいさつのメッセージが入ります。ダミーテキストが入ります。ごあいさつのメッセージが入ります。ダミーテキストが入ります。ごあいさつのメッセージが入ります。ダミーテキストが入ります。ごあいさつのメッセージが入ります。ダミーテキストが入ります。ごあいさつのメッセージが入ります。ごあいさつのメッセージが入ります。</div>

<!-- footer info -->
<div class="abs" style="left:62px;top:4725px;width:190px;display:flex;flex-direction:column;align-items:center;gap:14px">
  <div style="width:70px;height:70px;border-radius:50%;background:var(--teal)"></div>
  <div style="font-size:22px;font-weight:500;text-align:center;line-height:1.3">HARUNO<br>DENTAL CLINIC</div>
</div>
<div class="abs" style="left:313px;top:4700px;font-size:27px;font-weight:300">はるの歯科</div>
<div class="abs" style="left:313px;top:4758px;font-size:15px;line-height:2.1">〒000-0000　〇〇県〇〇市△△0-0-0<br>〇〇駅より徒歩1分<br>〇〇駅より徒歩1分</div>
<div class="abs" style="left:313px;top:4875px;display:flex;gap:12px;align-items:center">
  <svg width="24" height="24" viewBox="0 0 24 24"><path d="M6.6 10.8a15 15 0 0 0 6.6 6.6l2.2-2.2c.3-.3.7-.4 1-.2 1.1.4 2.3.6 3.6.6.6 0 1 .4 1 1V20c0 .6-.4 1-1 1A17 17 0 0 1 3 4c0-.6.4-1 1-1h3.5c.6 0 1 .4 1 1 0 1.3.2 2.5.6 3.6.1.3 0 .7-.2 1z" fill="var(--teal)"/></svg>
  <span style="font-size:32px;font-weight:300">000-555-0123</span>
</div>
<table class="hours abs" style="left:672px;top:4660px">
  <tr><td></td><th>月</th><th>火</th><th>水</th><th>木</th><th>金</th><th>土</th><th>日</th></tr>
  <tr><td>09:30 - 13:00</td><th>○</th><th>○</th><th>○</th><th>○</th><th>○</th><th>○</th><th>ー</th></tr>
  <tr><td>14:30 - 18:30</td><th>○</th><th>○</th><th>○</th><th>ー</th><th>○</th><th>ー</th><th>ー</th></tr>
</table>
<div class="abs" style="left:680px;top:4860px;font-size:13px">※水曜・日曜は定休（祝日は不定休）など注釈</div>
<div class="btn" style="left:682px;top:4909px;width:462px;height:66px">WEB予約はこちら<span class="dot"><svg width="10" height="10"><path d="M3 1l4 4-4 4" stroke="var(--teal)" stroke-width="1.8" fill="none"/></svg></span></div>

<div class="abs" style="left:0;top:5034px;width:1200px;height:1px;background:var(--line)"></div>

<!-- footer nav -->
<div class="fnav abs" style="left:157px;top:5082px"><h4>クリニック紹介</h4><ul>
  <li><span class="arrow-c"><svg width="8" height="8"><path d="M2 1l3 3-3 3" stroke="var(--teal)" stroke-width="1.5" fill="none"/></svg></span>院長、スタッフ紹介</li>
  <li><span class="arrow-c"><svg width="8" height="8"><path d="M2 1l3 3-3 3" stroke="var(--teal)" stroke-width="1.5" fill="none"/></svg></span>クリニック基本情報</li></ul></div>
<div class="fnav abs" style="left:400px;top:5082px"><h4>診療のご案内</h4><ul>
  <li><span class="arrow-c"><svg width="8" height="8"><path d="M2 1l3 3-3 3" stroke="var(--teal)" stroke-width="1.5" fill="none"/></svg></span>小児診療について</li>
  <li><span class="arrow-c"><svg width="8" height="8"><path d="M2 1l3 3-3 3" stroke="var(--teal)" stroke-width="1.5" fill="none"/></svg></span>一般診療について</li>
  <li><span class="arrow-c"><svg width="8" height="8"><path d="M2 1l3 3-3 3" stroke="var(--teal)" stroke-width="1.5" fill="none"/></svg></span>矯正治療について</li></ul></div>
<div class="fnav abs" style="left:626px;top:5082px"><h4>当クリニックの特徴</h4><ul><li>初診の方へ</li><li>アクセス</li><li>採用情報</li></ul></div>
<div class="fnav abs" style="left:858px;top:5082px"><h4>よくあるご質問</h4><ul><li>サイトマップ</li><li>プライバシーポリシー</li></ul></div>

<div class="abs" style="right:50px;top:5336px;font-size:12px;color:var(--sub)">@2019 HARUNO DENTAL CLINIC</div>

</body>
</html>
```